Certified Legal Nurse Consultant business needs a postcard design

Need a postcard that advertises to target market of attorneys. I am a registered nurse who helps lawyers with the medical issues on their cases. I want this card to highlight the benefit of my services versus the competition. Please see attached document for more info.
Updates

Reason: Many of the 20 designs I received were from the same designer, but just altered slightly. I was expecting ~20 original/unique designs. Thanks!

Target Market(s)

attorneys (lawyers)

Industry/Entity Type

Business

Font styles to use
Serif

Colors
3176b5
0355a3

Requirements
Must have
• my photo, business name and address, phone number, web address, description of how my business is better than the competition (see PDF file sent)

```html
<!DOCTYPE html>
<html lang="en">
<head>
<meta charset="utf-8">
<title>Postcard Design 01 – Certified Legal Nurse Consulting</title>
<link href="https://fonts.googleapis.com/css2?family=Roboto:wght@300;400;500&family=Roboto+Condensed:wght@300;400&family=PT+Sans:wght@400;700&display=swap" rel="stylesheet">
<style>
  :root {
    --board-light: #dcdcdc;
    --board-dark: #8c8c8c;
    --card-pale: #dcdff0;
    --ink: #262626;
    --ink-soft: #555a66;
    --front-dark: #151515;
    --front-deep: #05070f;
    --accent-blue: #3b5fd0;
    --band-blue: #2d4aa0;
    --link-blue: #4a6ee0;
    --navy: #2a3a8c;
    --panel-navy: #343f7c;
    --list-grey: #b8bccb;
    --rule-grey: #9a9a9a;
  }
  * { margin: 0; padding: 0; box-sizing: border-box; }
  html, body { width: 1200px; height: 1199px; overflow: hidden; }
  body {
    position: relative;
    background: radial-gradient(ellipse at 50% 40%, var(--board-light) 0%, #bdbdbd 55%, var(--board-dark) 100%);
    font-family: "Roboto", Arial, sans-serif;
  }
  .label {
    position: absolute;
    font-family: "PT Sans", Arial, sans-serif;
    color: #444;
    font-weight: 700;
    letter-spacing: -0.5px;
  }
  .label--front { left: 152px; top: 34px; font-size: 34px; }
  .label--back { left: 644px; top: 38px; font-size: 29px; letter-spacing: -1px; }

  .card {
    position: absolute;
    top: 89px;
    width: 463px;
    height: 922px;
    overflow: hidden;
    box-shadow: 0 6px 22px rgba(0,0,0,0.35);
  }
  /* Front */
  .card--front { left: 131px; background: linear-gradient(180deg, var(--front-dark) 0%, var(--front-dark) 60%, #0a0b12 100%); }
  .front__top { position: absolute; left: 0; top: 0; width: 100%; height: 107px; background: var(--card-pale); }
  .front__accent { position: absolute; left: 0; top: 107px; width: 15px; height: 49px; background: var(--accent-blue); }
  .front__name {
    position: absolute; left: 64px; top: 38px;
    font-size: 62px; line-height: 70px; font-weight: 300; color: var(--ink); letter-spacing: -1px; white-space: nowrap;
  }
  .front__firm {
    position: absolute; left: 65px; top: 112px;
    font-size: 44px; font-weight: 300; color: #fff; white-space: nowrap;
  }
  .front__photo { position: absolute; left: 0; top: 166px; width: 463px; height: 415px; display: block; }
  .front__band {
    position: absolute; left: 15px; top: 581px; width: 448px; height: 58px;
    background: var(--band-blue); color: #fff;
    font-family: "Roboto Condensed", Arial, sans-serif; font-size: 29px;
    display: flex; align-items: center; justify-content: center;
  }
  .front__list {
    position: absolute; left: 74px; top: 670px; list-style: none;
    font-family: "Roboto Condensed", Arial, sans-serif; font-weight: 300;
    font-size: 22px; line-height: 28px; color: var(--list-grey);
  }
  .front__list li { position: relative; padding-left: 36px; }
  .front__list svg { position: absolute; left: 0; top: 7px; }
  .front__footer {
    position: absolute; left: 0; bottom: 0; width: 100%; height: 65px;
    background: var(--front-deep);
    font-family: "Roboto Condensed", Arial, sans-serif; font-size: 30px; color: var(--link-blue);
    display: flex; align-items: center; justify-content: center;
  }
  /* Back */
  .card--back { left: 644px; background: var(--card-pale); }
  .back__name {
    position: absolute; left: 57px; top: 36px;
    font-size: 30px; font-weight: 300; line-height: 40px; color: var(--ink);
  }
  .back__role {
    position: absolute; left: 58px; top: 124px;
    font-size: 20px; font-weight: 300; line-height: 28px; color: var(--ink-soft);
  }
  .back__stamp { position: absolute; left: 301px; top: 34px; width: 123px; height: 152px; border: 2px solid #8a8a8a; }
  .back__rule { position: absolute; left: 46px; width: 378px; height: 1px; background: var(--rule-grey); }
  .back__heading {
    position: absolute; font-size: 26px; font-weight: 400; color: var(--navy); letter-spacing: -0.3px;
  }
  .back__heading--services { left: 57px; top: 463px; }
  .back__heading--contact { left: 63px; top: 668px; }
  .back__underline { position: absolute; left: 57px; top: 497px; right: 0; height: 2px; background: var(--navy); }
  .back__services {
    position: absolute; left: 63px; top: 513px; width: 352px;
    font-size: 18px; line-height: 24px; color: var(--ink); text-align: justify;
  }
  .back__panel { position: absolute; left: 0; top: 704px; width: 100%; height: 218px; background: var(--panel-navy); color: #fff; }
  .back__phone { position: absolute; left: 92px; top: 24px; display: flex; align-items: center; gap: 6px; font-size: 27px; font-weight: 500; }
  .back__address { position: absolute; left: 95px; top: 74px; font-size: 20px; font-weight: 300; line-height: 25px; }
  .back__email { position: absolute; left: 95px; top: 165px; display: flex; align-items: center; gap: 9px; font-size: 18.5px; font-weight: 400; }

  /* Presentation captions */
  .caption-box {
    position: absolute; left: 0; top: 1035px; width: 343px; height: 84px; background: #111;
    color: #fff; font-family: "PT Sans", Arial, sans-serif;
  }
  .caption-box__title { position: absolute; left: 53px; top: 20px; font-size: 32px; letter-spacing: -0.8px; }
  .caption-box__num { position: absolute; left: 289px; top: 10px; font-size: 36px; color: var(--link-blue); }
  .caption-size {
    position: absolute; left: 55px; top: 1133px;
    font-family: "PT Sans", Arial, sans-serif; font-size: 27px; color: #333; letter-spacing: -0.8px;
  }
  .caption-note {
    position: absolute; left: 470px; top: 1045px; width: 640px;
    font-family: "PT Sans", Arial, sans-serif; font-size: 20.5px; line-height: 25.5px; color: #333; letter-spacing: -0.9px;
  }
  .caption-note strong { color: #222; }
</style>
</head>
<body>
  <div class="label label--front">Front</div>
  <div class="label label--back">Back (option 01 - similar to postcard)</div>

  <section class="card card--front">
    <div class="front__top"></div>
    <div class="front__accent"></div>
    <svg class="front__photo" role="img" aria-label="Portrait photograph of the consultant against a dark studio backdrop" viewBox="0 0 463 415">
      <defs>
        <radialGradient id="photoTone" cx="50%" cy="45%" r="60%">
          <stop offset="0" stop-color="#4a3a30"/>
          <stop offset="0.6" stop-color="#2a2624"/>
          <stop offset="1" stop-color="#1a1a1a"/>
        </radialGradient>
      </defs>
      <rect width="463" height="415" fill="url(#photoTone)"/>
    </svg>
    <div class="front__name">M. Halvorsen</div>
    <div class="front__firm">&amp; Associates, LLC</div>
    <div class="front__band">Certified Legal Nurse Consulting</div>
    <ul class="front__list">
      <li><svg width="18" height="16" viewBox="0 0 18 16"><path d="M1 9 L6 14 L17 1" fill="none" stroke="#3b5fd0" stroke-width="2"/></svg>Screen cases for merit</li>
      <li><svg width="18" height="16" viewBox="0 0 18 16"><path d="M1 9 L6 14 L17 1" fill="none" stroke="#3b5fd0" stroke-width="2"/></svg>Develop medical summaries</li>
      <li><svg width="18" height="16" viewBox="0 0 18 16"><path d="M1 9 L6 14 L17 1" fill="none" stroke="#3b5fd0" stroke-width="2"/></svg>Research authoritative literature</li>
      <li><svg width="18" height="16" viewBox="0 0 18 16"><path d="M1 9 L6 14 L17 1" fill="none" stroke="#3b5fd0" stroke-width="2"/></svg>Locate testifying experts</li>
      <li><svg width="18" height="16" viewBox="0 0 18 16"><path d="M1 9 L6 14 L17 1" fill="none" stroke="#3b5fd0" stroke-width="2"/></svg>Identify adherences to and<br>deviations from standard of care</li>
    </ul>
    <div class="front__footer">www.halvorsen-associates.com</div>
  </section>

  <section class="card card--back">
    <div class="back__name">M. Halvorsen<br>&amp; Associates</div>
    <div class="back__role">Certified Legal<br>Nurse Consultant</div>
    <div class="back__stamp"></div>
    <div class="back__rule" style="top:251px"></div>
    <div class="back__rule" style="top:303px"></div>
    <div class="back__rule" style="top:356px"></div>
    <div class="back__rule" style="top:408px"></div>
    <h2 class="back__heading back__heading--services">Our Services</h2>
    <div class="back__underline"></div>
    <p class="back__services">as a Certified Legal Nurse Consultant (CLNC) and Registered Nurse (RN) with over 26 years experience, I help attorneys effectively develop the medical-related issues in their cases.</p>
    <h2 class="back__heading back__heading--contact">Contact</h2>
    <div class="back__panel">
      <div class="back__phone">
        <svg width="24" height="30" viewBox="0 0 24 30"><path d="M5 2 L9 1 L12 9 L9 11 C10 16 13 21 16 24 L19 22 L23 28 L19 30 C10 28 2 15 2 5 Z" fill="#fff"/></svg>
        (555) 204-7781
      </div>
      <div class="back__address">M. Halvorsen &amp; Associates LLC<br>1820 Meadowlark Lane<br>Lakeview, MN 55000</div>
      <div class="back__email">
        <svg width="23" height="16" viewBox="0 0 23 16"><rect x="1" y="1" width="21" height="14" fill="none" stroke="#fff" stroke-width="1.8"/><path d="M1 1 L11.5 9 L22 1 M1 15 L8.5 7 M22 15 L14.5 7" fill="none" stroke="#fff" stroke-width="1.5"/></svg>
        anna@halvorsen-associates.com
      </div>
    </div>
  </section>

  <div class="caption-box">
    <span class="caption-box__title">Postcard Design</span>
    <span class="caption-box__num">01</span>
  </div>
  <div class="caption-size">140 x 279 mm &nbsp;|&nbsp; Portrait Orientation</div>
  <p class="caption-note"><strong>Please note:</strong> Seeing that 140 x 279mm is not a standard US mail postcard size, I tried to provide the best solution to present the content, keeping the postcard look. Thanks for the opportunity. Feedback is always appreciated.</p>
</body>
</html>
```